Banner for promote service of debit card

We are PagaVelo and we need the banners to be posted on the facebook and instagram pages.
We want something to communicate that it is an exclusive debit card full of services.
Low commissions.
Our competitors:
https://www.nortapay-pagos.it/it/home.html
https://www.zelkor-conti.it/it/
https://www.fotoreelz.it/serravanbank/
sendquillo
maybe some banner that makes the idea of a convenient debit card that everyone can use.
Girls enjoying card shopping.
Please check also website for slogans and phrases to use
https://www.pagavelo-carta.it/
Should show the services.
We must convey that it is a fast, simple card that guarantees privacy.
We need strong banners that attract people as these ban will be sponsored on instagram and facebook
Target Market(s)
People 18-35 y
Open Bank account. low commissions. Easy to use. No limits. 100% Privacy.
Requirements
Must have
- Written in Italian.

```html
<!DOCTYPE html>
<html lang="it">
<head>
<meta charset="UTF-8">
<title>PagaVelo – Una carta per tutti</title>
<link href="https://fonts.googleapis.com/css2?family=Montserrat:wght@500;600;700&display=swap" rel="stylesheet">
<style>
  :root {
    --bg-start: #8f2a93;
    --bg-mid: #c2237c;
    --bg-end: #ec2f55;
    --accent-orange: #f2583e;
    --headline-yellow: #f8e27c;
    --text-white: #ffffff;
    --brand-grey: #6b6b6b;
    --panel-white: #ffffff;
  }
  * { margin: 0; padding: 0; box-sizing: border-box; }
  html, body { width: 1200px; height: 457px; overflow: hidden; }
  body { font-family: "Montserrat", sans-serif; }

  .banner {
    position: relative;
    width: 1200px;
    height: 457px;
    overflow: hidden;
    background: linear-gradient(90deg, var(--bg-start) 0%, var(--bg-mid) 50%, var(--bg-end) 100%);
  }

  /* Brand panel */
  .brand-panel {
    position: absolute;
    left: -30px;
    top: -30px;
    width: 395px;
    height: 252px;
    background: var(--panel-white);
    border: 9px solid var(--accent-orange);
    border-radius: 0 0 44px 0;
  }
  .brand {
    position: absolute;
    left: 0;
    top: 78px;
    width: 320px;
    display: flex;
    flex-direction: column;
    align-items: center;
    gap: 14px;
  }
  .brand-dot {
    width: 56px;
    height: 56px;
    border-radius: 50%;
    background: var(--accent-orange);
  }
  .brand-name {
    font-weight: 700;
    font-size: 36px;
    color: var(--brand-grey);
    letter-spacing: 0.5px;
  }

  /* Message */
  .message {
    position: absolute;
    left: 423px;
    top: 48px;
    color: var(--text-white);
  }
  .headline {
    color: var(--headline-yellow);
    font-weight: 700;
    font-size: 37px;
    line-height: 1.1;
  }
  .subhead {
    color: var(--headline-yellow);
    font-weight: 700;
    font-size: 32px;
    line-height: 1.2;
    margin-top: 4px;
  }
  .claims {
    list-style: none;
    margin-top: 20px;
    font-weight: 500;
    font-size: 21px;
    line-height: 31px;
  }
  .promise {
    margin-top: 32px;
    color: var(--headline-yellow);
    font-weight: 700;
    font-size: 25px;
    line-height: 34px;
  }
  .tagline {
    margin-top: 10px;
    font-weight: 700;
    font-size: 18px;
    line-height: 24px;
  }

  /* Card chooser */
  .card-chooser {
    position: absolute;
    left: 44px;
    top: 300px;
    color: var(--text-white);
  }
  .card-chooser-title {
    font-weight: 600;
    font-size: 17px;
    margin-left: 6px;
    margin-bottom: 10px;
  }
  .card-options { display: flex; gap: 7px; }
  .card-option { width: 88px; }
  .card-art {
    width: 88px;
    height: 58px;
    border-radius: 5px;
    border: 1.5px solid rgba(255,255,255,0.8);
  }
  .card-art.cash { background: linear-gradient(135deg, #f4b2b8, #e97a8c); }
  .card-art.travel { background: linear-gradient(135deg, #fde26a, #f5a623); }
  .card-art.partner { background: linear-gradient(135deg, #3bb6c9, #1d6f9c); }
  .card-label {
    margin-top: 6px;
    font-weight: 700;
    font-size: 10px;
    line-height: 13px;
  }
  .card-label span { display: block; font-weight: 500; }

  /* Lifestyle photo */
  .photo-frame {
    position: absolute;
    left: 808px;
    top: 12px;
    width: 420px;
    height: 470px;
    background: var(--accent-orange);
    border-radius: 44px 0 0 0;
  }
  .photo {
    position: absolute;
    left: 820px;
    top: 22px;
    width: 400px;
    height: 460px;
    border-radius: 36px 0 0 0;
    background: linear-gradient(160deg, #e9ded3 0%, #c9b3a3 45%, #8f7468 100%);
  }
</style>
</head>
<body>
  <main class="banner">
    <div class="brand-panel">
      <div class="brand">
        <div class="brand-dot"></div>
        <div class="brand-name">PagaVelo</div>
      </div>
    </div>

    <section class="message">
      <h1 class="headline">All in One!</h1>
      <h2 class="subhead">Una carta per tutti</h2>
      <ul class="claims">
        <li>Enjoy your cart!</li>
        <li>Fai quello che vuoi.</li>
        <li>Nessun limite.</li>
        <li>Nessun controllo.</li>
      </ul>
      <p class="promise">Privacy garantita.<br>Credito assicurato.</p>
      <p class="tagline">Usala come vuoi.<br>Senza essere controllato</p>
    </section>

    <section class="card-chooser">
      <p class="card-chooser-title">Scegli la tua carta perfetta</p>
      <div class="card-options">
        <div class="card-option">
          <div class="card-art cash" role="img" aria-label="Carta di debito rosa Cash Rewards"></div>
          <p class="card-label">Cash Rewards<span>First Year Free</span></p>
        </div>
        <div class="card-option">
          <div class="card-art travel" role="img" aria-label="Carta di debito gialla Travel Rewards"></div>
          <p class="card-label">Travel Rewards<span>10,000 Points</span></p>
        </div>
        <div class="card-option">
          <div class="card-art partner" role="img" aria-label="Carta di debito azzurra Partner Rewards"></div>
          <p class="card-label">Partner Rewards<span>2,000 Points</span></p>
        </div>
      </div>
    </section>

    <div class="photo-frame"></div>
    <div class="photo" role="img" aria-label="Ragazza sorridente in un negozio di abbigliamento con una carta e una borsa della spesa"></div>
  </main>
</body>
</html>
```